Lone Mesa Haulworks Garage web site for repairs,Parts, Accessories and Off Road

Need a wed site design for our light duty truck repair shop, also need to be able to sell our products from this page as well. Has our logo as the headliner and brief description of what we do and our history. An example of what we would want it to work like can be seen at www.garvinsfuelworks.example . This is a good example of style and accesses ability to buy parts we have.

Target Market(s)

Light duty Diesel truck owners(Brell,Kastor,Vantorine)

Industry/Entity Type

Shop

Number of Pages Required

3 page

Font styles to use
Other font styles liked:
• The same font as our logo

Requirements
Must have
• A little about the shop and all of our services,availability to purchase our products, also a map of where we are located.
Nice to have
• I like the design of www.Garvinsfuelworks.example. Its easy to use and very descriptive of parts available

```html
<!DOCTYPE html>
<html lang="en">
<head>
<meta charset="utf-8">
<title>Lone Mesa Haulworks Garage</title>
<link href="https://fonts.googleapis.com/css2?family=Open+Sans:wght@400;600;700&display=swap" rel="stylesheet">
<style>
:root{
  --navy:#0d2f5e;
  --navy-deep:#0a2549;
  --blue:#1d5fa8;
  --blue-bright:#2a76c6;
  --grey-band:#e6e7e9;
  --text:#5a6470;
  --white:#ffffff;
  --muted:#a9bbd3;
}
*{margin:0;padding:0;box-sizing:border-box}
html,body{width:828px;height:1200px;overflow:hidden;background:var(--white)}
body{position:relative;font-family:"Open Sans",Arial,sans-serif;color:var(--text)}
.abs{position:absolute}

/* hero */
.hero-photo{left:0;top:0;width:828px;height:415px;
  background:linear-gradient(180deg,#a8b6c6 0%,#d4dae2 35%,#8a8f96 62%,#555a60 100%)}
.site-nav{left:0;top:0;width:828px;height:55px;background:rgba(10,37,73,.92);display:flex;align-items:center;padding:0 22px}
.brand{display:flex;align-items:center;gap:7px;color:var(--white);font-weight:700;font-size:13px;letter-spacing:.3px}
.brand-mark{width:12px;height:12px;background:var(--blue-bright)}
.nav-links{margin-left:auto;display:flex;gap:28px;list-style:none}
.nav-links li{color:var(--white);font-size:10px;font-weight:600;letter-spacing:.4px}

.service-strip{left:77px;top:305px;width:673px;height:110px;display:flex;box-shadow:0 6px 14px rgba(0,0,0,.3)}
.service-text{width:170px;height:110px;background:var(--blue);color:var(--white);padding:12px 14px}
.service-text h3{font-size:10px;font-weight:700;margin-bottom:6px}
.service-text p{font-size:7.5px;line-height:11px;color:#d5e3f3}
.service-text .btn-more{margin-top:10px}
.service-text.right{text-align:right}
.service-photo{width:166px;height:110px;background:linear-gradient(135deg,#3b3f45,#8a8d91 50%,#2b2e33)}
.btn-more{display:inline-flex;align-items:center;gap:6px;font-size:7.5px;font-weight:700;color:var(--white);background:var(--navy-deep);padding:5px 8px}

/* about */
.section-title{width:828px;text-align:center;color:var(--blue);font-weight:700;font-size:19px;letter-spacing:.5px}
.about-title{top:460px;left:0}
.about-text{top:497px;left:134px;width:560px;text-align:center;font-size:8.5px;line-height:13px}
.about-btn{top:548px;left:378px}

/* products */
.product-band{left:0;top:607px;width:828px;height:331px;background:var(--grey-band)}
.products-title{top:628px;left:0}
.product-card{top:676px;width:152px;height:221px;background:var(--white);box-shadow:0 4px 10px rgba(0,0,0,.18)}
.product-photo{width:152px;height:152px;background:linear-gradient(135deg,#2e3135,#9ea2a7 50%,#3a3d41)}
.product-info{text-align:center;padding-top:12px}
.product-info h4{font-size:8px;font-weight:700;color:var(--blue);margin-bottom:6px}
.product-info p{font-size:7.5px;line-height:11px}

/* footer */
.site-footer{left:0;top:938px;width:828px;height:235px;background:var(--navy)}
.footer-col{top:962px;color:var(--white)}
.footer-col h5{font-size:14px;font-weight:400;margin-bottom:12px}
.footer-col p{font-size:8px;line-height:12px;color:var(--muted)}
.quick-links{list-style:none}
.quick-links li{font-size:7.5px;line-height:13px;color:var(--muted)}
.subscribe{display:flex;margin-top:14px}
.subscribe .field{width:128px;height:22px;background:var(--white);font-size:7.5px;color:#8c96a3;padding:6px 7px}
.subscribe .submit{height:22px;background:var(--navy-deep);color:var(--white);font-size:7.5px;font-weight:700;padding:6px 8px}
.social-row{display:flex;gap:9px}
.social-dot{width:24px;height:24px;border:1.5px solid var(--muted);border-radius:50%}
.footer-base{left:0;top:1173px;width:828px;height:27px;background:var(--navy-deep);color:var(--muted);font-size:7.5px;text-align:center;line-height:27px}
</style>
</head>
<body>

<div class="abs hero-photo" role="img" aria-label="Photo of a row of heavy trucks parked side by side on an open road under a cloudy sky"></div>

<header class="abs site-nav">
  <div class="brand"><span class="brand-mark"></span>Lone Mesa Haulworks Garage</div>
  <ul class="nav-links">
    <li>HOME</li><li>SERVICE</li><li>ABOUT US</li><li>TESTIMONIALS</li><li>BLOG</li><li>CONTACT</li>
  </ul>
</header>

<section class="abs service-strip">
  <div class="service-text">
    <h3>TRUCK REPAIR</h3>
    <p>Diesel engine checks, brake work and fuel system tune ups done right.</p>
    <span class="btn-more">READ MORE
      <svg width="5" height="6" viewBox="0 0 5 6"><path d="M0 0L5 3L0 6Z" fill="#fff"/></svg></span>
  </div>
  <div class="service-photo" role="img" aria-label="Close-up photo of a mechanic working on a truck engine"></div>
  <div class="service-photo" role="img" aria-label="Close-up photo of a diesel engine block"></div>
  <div class="service-text right">
    <h3>TRUCK REPAIR</h3>
    <p>Transmission, axle and suspension repair for light duty diesel trucks.</p>
    <span class="btn-more">READ MORE
      <svg width="5" height="6" viewBox="0 0 5 6"><path d="M0 0L5 3L0 6Z" fill="#fff"/></svg></span>
  </div>
</section>

<h2 class="abs section-title about-title">ABOUT US</h2>
<p class="abs about-text">We are a family run shop serving light duty diesel truck owners for over twenty years. Our crew handles engine repair, performance parts, accessories and off road builds, with honest quotes and fast turnaround. Stop by the garage or shop our parts online any time of day.</p>
<span class="abs btn-more about-btn">READ MORE
  <svg width="5" height="6" viewBox="0 0 5 6"><path d="M0 0L5 3L0 6Z" fill="#fff"/></svg></span>

<div class="abs product-band"></div>
<h2 class="abs section-title products-title">SELL PRODUCTS</h2>

<article class="abs product-card" style="left:69px">
  <div class="product-photo" role="img" aria-label="Product photo of a turbo charger"></div>
  <div class="product-info"><h4>TURBO CHARGER</h4><p>LIST PRICE : $536.00</p><p>OUR PRICE : $506.00</p></div>
</article>
<article class="abs product-card" style="left:243px">
  <div class="product-photo" role="img" aria-label="Product photo of a fuel injector"></div>
  <div class="product-info"><h4>FUEL INJECTOR</h4><p>LIST PRICE : $536.00</p><p>OUR PRICE : $506.00</p></div>
</article>
<article class="abs product-card" style="left:419px">
  <div class="product-photo" role="img" aria-label="Product photo of a brake rotor"></div>
  <div class="product-info"><h4>BRAKE ROTOR</h4><p>LIST PRICE : $536.00</p><p>OUR PRICE : $506.00</p></div>
</article>
<article class="abs product-card" style="left:593px">
  <div class="product-photo" role="img" aria-label="Product photo of a transmission gear set"></div>
  <div class="product-info"><h4>GEAR SET</h4><p>LIST PRICE : $536.00</p><p>OUR PRICE : $506.00</p></div>
</article>

<footer class="abs site-footer"></footer>

<div class="abs footer-col" style="left:69px;width:150px">
  <h5>About Us</h5>
  <p>Honest diesel repair and quality truck parts from a local crew that knows your rig inside and out.</p>
</div>
<div class="abs footer-col" style="left:262px">
  <h5>Quick link</h5>
  <ul class="quick-links">
    <li>HOME</li><li>SERVICE</li><li>ABOUT US</li><li>TESTIMONIALS</li><li>BLOG</li><li>CONTACT</li>
  </ul>
</div>
<div class="abs footer-col" style="left:424px;width:180px">
  <h5>Newsletter subscribe</h5>
  <p>Sign up for our newsletter to get new parts, deals and shop news.</p>
  <div class="subscribe"><span class="field">Your email</span><span class="submit">SUBMIT</span></div>
</div>
<div class="abs footer-col" style="left:640px">
  <h5>Social</h5>
  <div class="social-row"><span class="social-dot"></span><span class="social-dot"></span><span class="social-dot"></span></div>
</div>

<div class="abs footer-base">2015 Lone Mesa Haulworks Garage</div>

</body>
</html>
```